Content Writing Website Project and Logo Name is FindSterlingEssays

Color codes in the images. Incase anything is needed let me know.
Colors to use:
- #1F73B7
- #00B2FF
- #DDA01E
- #E6F4F1
For the above the fold banner use a gradient with these 2 colors #1F73B7 & #00B2FF
Above the Fold
Header
- Logo “FindSterlingEssays which will be bolded. The slogan – Writing platform –“
- Services (will have a dropdown)
- Reviews
- Writers
- Resources which will have a drop down
- Login Button
- Hire Writer Button
Value Proposition
Top Company in Research, Summary Writing Services.
We build trust through quality and professional services.

Social Proof
- 455 Satisfied clients
- 100 + Professional writers
- 1000 jobs done
- 5 stars icon check out our customer reviews (4.9/5 from 1000 ratings)
- Video icon then How it works link for a pop-up video
Infographic
Infographic will be an owl or a dolphin and well integrated CTA “Order Now” Something that will improve on trust and allow engagement.

Below Fold
Rating
“Trusted by 100+ students Around the World”. Images attached on how it will look like. Will have 2 sections, one showing sites reviews and the other reviews from fair meter.

Writers
“An Exclusive Network of Top Writers.”
Will show 4 profiles in one row with an option to “See all Professionals.”
I have attached profile guide to this part

Features & Benefits
Will show 6 of them with content of 5-6 lines. Will be displayed in 3 rows and 2 columns. Also allowed to be creative.
Will have an Order Now button

Guarantee
- Revision
- Money Back
- Plagiarism Free

Why Us?
Check the image labeled section 5 and maintain the layout.

- Proof of Quality. “Check our Samples, Client Reviews and Identity Verification.”
- Great prices For Superb Quality. "You Can't Afford to Get Overcharged. Satisfaction is Guaranteed once you order with Us."
- Safe and Secure. We let you focus on your work as we help protect your data and privacy. We are here 24/7 for any support needed.
- Highest Repeat Client Rate. 90% Repeat Order Rate as a result of Professionalism and Originality Guaranteed.
Below is a call-to-action button, “Order Now.”

How it Works
- Fill order (will have content)
- Choose writer (will have content)
- Editors check (will have content)
- Final delivery (will have content)
Will have a Hire Writer Button
Brief
“Welcome to FindSterlingEssays: Top Research & Summary Writing Service.” Will write what the company is about and what we offer. Will be scrollable to allow to fit more words without making the landing page long.

Samples
Will show a total of 8 samples in 2 rows and 4 columns, which will be in squares which will have topic, no. of pages, sources, subject.

FAQs
Will answer 10 questions. Sent designs

Keywords
Will display a list of keywords here.
Footer

Inspirations
https://tutorwren.example/
https://draftsheron.example/
https://lernolix.example/
https://textcrest.example/
Updates

Hello, I have updated a How it Works by providing the content for it in a wireframe. Kindly note the writers profile attached are what am using currently and would love to retain as it is.

I have also attached the badges and the profile files just incase they are needed to integrate in the landing page design instead of creating afresh

Target Market(s)

Content Writing, Research and Summary Writing Clients

Industry/Entity Type

Content Writing, Research & Summary

Font styles to use
Sans Serif

Colors

Designer to choose colors to be used in the design.

Requirements
Must have
• Bright colors that portrays trust and should look more professional and neat
Nice to have
• Information should be much visible and easy on the client, and have flow.

```html
<!DOCTYPE html>
<html lang="en">
<head>
<meta charset="utf-8">
<title>FindSterlingEssays – Research &amp; Summary Writing</title>
<link href="https://fonts.googleapis.com/css2?family=Libre+Caslon+Text:wght@400;700&family=Poppins:wght@300;400;500;600&display=swap" rel="stylesheet">
<style>
:root{
  --blue:#1F73B7;
  --sky:#00B2FF;
  --gold:#DDA01E;
  --mint:#E6F4F1;
  --teal:#4fd3ad;
  --navy:#16355f;
  --ink:#1d3557;
  --text:#4a5566;
  --muted:#8a94a3;
  --line:#e3e8ee;
  --soft:#f4f7fa;
}
*{margin:0;padding:0;box-sizing:border-box}
html,body{width:1200px;height:5259px;overflow:hidden}
body{font-family:"Poppins",sans-serif;color:var(--text);background:#fff;position:relative}
section,footer{position:relative;width:1200px;overflow:hidden}
.abs{position:absolute}
.btn{position:absolute;display:flex;align-items:center;justify-content:center;font-size:10px;font-weight:600;letter-spacing:.08em;text-transform:uppercase;color:#fff;background:var(--teal);border-radius:2px}
.stars{color:var(--gold);letter-spacing:1px}
h2.title{font-family:"Libre Caslon Text",serif;font-weight:400;color:var(--ink);font-size:29px;text-align:center;position:absolute;left:0;width:1200px}

/* hero */
.hero{height:592px;background:linear-gradient(120deg,var(--blue) 0%,#1d8fc6 45%,#3cd2a8 100%);color:#fff}
.logo{left:30px;top:30px;font-family:"Libre Caslon Text",serif;font-weight:700;font-size:19px;color:#fff}
.logo small{display:block;font-family:"Poppins",sans-serif;font-weight:400;font-size:10px;color:#7ff0c8;text-align:right;margin-top:2px}
.nav{left:404px;top:34px;display:flex;gap:58px;font-size:11px}
.nav span svg{vertical-align:middle;margin-left:3px}
.login{left:932px;top:24px;width:120px;height:36px;background:#fff;color:var(--blue)}
.hire{left:1056px;top:24px;width:114px;height:36px}
.hero h1{left:163px;top:128px;font-family:"Libre Caslon Text",serif;font-weight:400;font-size:41px;line-height:52px}
.hero .lead{left:163px;top:305px;font-size:14px}
.hero .order{left:163px;top:346px;width:112px;height:36px}
.play{left:290px;top:348px;width:33px;height:33px;border-radius:50%;background:var(--teal);display:flex;align-items:center;justify-content:center}
.rate{left:663px;top:193px;width:148px;height:90px;background:#fff;color:var(--ink);text-align:center;padding-top:10px}
.rate b{font-size:24px;font-weight:500;display:block;line-height:30px}
.rate i{font-style:normal;font-size:12px;display:block;line-height:16px}
.rate small{font-size:11px;display:block;margin-top:6px;line-height:14px}
.mascot{left:795px;top:70px;width:380px;height:340px;border-radius:40% 40% 30% 30%;background:radial-gradient(circle at 50% 40%,#2a5a8a 0%,#24709e 40%,rgba(40,160,190,.0) 72%)}
.stat{top:478px;width:200px;text-align:center}
.stat b{font-weight:300;font-size:42px;display:block;line-height:48px}
.stat span{font-size:12px}

/* reviews */
.reviews{height:388px;background:#fbfcfe}
.reviews h2{left:163px;top:108px;font-family:"Libre Caslon Text",serif;font-weight:400;font-size:30px;line-height:37px;color:var(--ink)}
.reviews .rated{left:163px;top:230px;font-size:10px;font-weight:600;color:var(--ink)}
.fair{left:163px;top:254px;font-size:12px;font-weight:600;color:var(--ink);display:flex;align-items:center;gap:5px}
.fair i{width:10px;height:10px;background:var(--teal);display:block}
.arrow{top:265px;width:26px;height:26px;border-radius:50%;border:1px solid var(--blue);display:flex;align-items:center;justify-content:center}
.rcard{top:88px;width:245px;height:215px;background:#fff;box-shadow:0 4px 18px rgba(30,60,100,.08);padding:18px 16px}
.rcard .rs{font-size:13px;line-height:14px}
.rcard h4{font-size:11px;font-weight:600;color:var(--ink);margin:16px 0 8px}
.rcard p{font-size:10px;line-height:20px;color:var(--text)}
.rcard .who{position:absolute;left:16px;bottom:18px;display:flex;align-items:center;gap:10px;font-size:10px}
.rcard .who i{width:26px;height:26px;border-radius:50%;background:var(--blue);color:#fff;font-size:9px;font-style:normal;display:flex;align-items:center;justify-content:center}

/* writers */
.writers{height:582px}
.wcard{top:121px;width:210px;height:334px;border:1px solid var(--line);background:#fff}
.wcard .head{height:48px;background:#d9ecfb;position:relative}
.wcard .av{position:absolute;left:14px;top:14px;width:58px;height:58px;border-radius:50%;background:linear-gradient(#c9d4de,#9fb0c0);border:3px solid #fff}
.wcard .nm{position:absolute;left:94px;top:16px;font-size:11px;font-weight:600;color:var(--ink)}
.wcard .nm small{display:block;font-weight:400;font-size:9px;color:var(--muted)}
.wcard .body{padding:42px 18px 0;font-size:10px;line-height:31px}
.wcard .id{font-size:14px;color:var(--muted);line-height:30px}
.wcard .k{color:var(--blue)}
.wcard b{font-weight:600;color:var(--ink)}
.badges{display:flex;gap:6px;margin-top:4px}
.badges i{width:17px;height:17px;border-radius:50%;border:2px solid #5b7fa6;display:block}
.badges i:nth-child(4){border-color:#e39b3a}
.badges i:nth-child(5){border-color:#e06c4a}
.vp{font-size:9px;font-weight:600;color:var(--blue);text-decoration:underline;letter-spacing:.05em}
.seeall{left:494px;top:486px;width:194px;height:34px}

/* features */
.features{height:514px;background:linear-gradient(120deg,#3aa9e8 0%,#4fc0ef 50%,#2f9ede 100%);color:#fff}
.feat{width:230px;display:flex;gap:10px}
.feat .ic{flex:none;width:20px;height:20px;border-radius:50%;background:#fff;display:flex;align-items:center;justify-content:center}
.feat h4{font-size:12px;font-weight:500;margin-bottom:4px;margin-top:2px}
.feat p{font-size:10px;line-height:21px;color:#e3f4ff}

/* why */
.why{height:624px}
.why h2{left:163px;top:86px;font-family:"Libre Caslon Text",serif;font-weight:400;font-size:29px;color:var(--ink)}
.wi{left:163px;width:500px}
.wi h4{font-size:14px;font-weight:500;color:var(--ink);display:flex;align-items:center;gap:8px;margin-bottom:10px}
.wi h4:before{content:"";width:5px;height:5px;border-radius:50%;background:var(--teal)}
.wi p{font-size:11px;line-height:22px}
.why .order{left:163px;top:502px;width:112px;height:36px;background:var(--blue)}
.photo{left:708px;top:62px;width:492px;height:500px;background:linear-gradient(135deg,#d6dbe0,#b8c0c8 55%,#e8ecef)}

/* how */
.how{height:389px;background:linear-gradient(180deg,#9fe2cd,#8fdcc6)}
.how h2{top:66px}
.pill{position:absolute;background:#fff;border:1px solid #cfe7df;border-radius:24px;font-size:8px;line-height:11px;color:var(--text);display:flex;align-items:center;justify-content:center;text-align:center;padding:0 10px;box-shadow:0 3px 10px rgba(0,80,70,.08)}
.pill.final{background:var(--blue);color:#fff;font-size:10px;line-height:14px;border:0}

/* welcome */
.welcome{height:341px}
.welcome h2{top:60px;line-height:40px}
.welcome .sub{top:150px;width:1200px;text-align:center;font-size:11px;font-weight:600;color:var(--ink)}
.welcome p{left:310px;top:180px;width:580px;text-align:center;font-size:11px;line-height:22px}

/* brief scroll */
.brief{height:377px;background:var(--soft)}
.panel{left:200px;top:45px;width:780px;height:332px;background:#fff}
.panel .dash{position:absolute;left:60px;top:38px;width:14px;height:3px;background:var(--ink)}
.bcard{top:57px;width:310px;height:275px;border:1px solid var(--line);border-bottom:0;border-radius:6px 6px 0 0;padding:30px 30px 0}
.bcard h4{font-size:10.5px;font-weight:600;color:var(--ink);margin-bottom:14px}
.bcard p{font-size:9.5px;line-height:20px}
.bcard .bar{position:absolute;right:10px;top:24px;width:3px;height:16px;background:var(--ink)}

/* faq */
.faq{height:582px}
.faq h2{top:74px}
.q{width:300px;display:flex;gap:14px}
.q i{flex:none;width:18px;height:18px;border-radius:50%;background:var(--blue);color:#fff;font-style:normal;font-size:10px;font-weight:600;display:flex;align-items:center;justify-content:center}
.q h4{font-size:11px;font-weight:500;color:var(--ink);line-height:17px;margin-bottom:6px}
.q p{font-size:8.5px;line-height:17px}

/* keywords */
.keys{height:449px}
.keys h2{top:72px}
.kw{width:200px;font-size:10px;padding-bottom:16px;border-bottom:1px solid var(--line)}

/* footer */
footer{height:421px;background:linear-gradient(180deg,#153b68,#112f55);color:#fff}
.guar{left:228px;top:74px;font-size:14px;font-weight:500}
.gbox{top:42px;width:183px;height:80px;border:1px solid rgba(255,255,255,.55);display:flex;align-items:center;justify-content:center;gap:14px;font-size:11px;font-weight:500}
.flogo{left:165px;top:172px;font-family:"Libre Caslon Text",serif;font-weight:700;font-size:17px}
.flogo small{display:block;text-align:right;font-family:"Poppins",sans-serif;font-weight:400;font-size:10px;margin-top:2px}
.fabout{left:155px;top:232px;width:225px;font-size:9px;line-height:19px;color:#c6d3e4}
.flinks{left:527px;top:168px;font-size:9.5px;line-height:20.5px;color:#dfe8f3}
.fcontact{left:770px;top:196px;font-size:10px;color:#dfe8f3}
.fcontact div{display:flex;gap:14px;align-items:flex-start;margin-bottom:26px;line-height:16px}
.copy{left:0;top:398px;width:1200px;text-align:center;font-size:9px;color:#c6d3e4}
</style>
</head>
<body>

<section class="hero">
  <div class="abs logo">FindSterlingEssays<small>Writing platform</small></div>
  <nav class="abs nav">
    <span>Services</span><span>Reviews</span><span>Writers</span>
    <span>Resources<svg width="8" height="6" viewBox="0 0 8 6"><path d="M1 1l3 3 3-3" stroke="#fff" fill="none" stroke-width="1.2"/></svg></span>
  </nav>
  <a class="btn login">Login</a>
  <a class="btn hire">Hire Writer</a>
  <h1 class="abs">Top Company in<br>Research, Summary<br>Writing Services.</h1>
  <p class="abs lead">We build trust through quality and professional services.</p>
  <a class="btn order">Order Now</a>
  <div class="abs play"><svg width="12" height="12" viewBox="0 0 12 12"><path d="M3 1.5l7 4.5-7 4.5z" fill="#fff"/></svg></div>
  <div class="abs rate"><b>4.9/5</b><i class="stars">★★★★★</i><small>from 1000 ratings</small></div>
  <div class="abs mascot" role="img" aria-label="Owl mascot in a graduation cap perched on an open book"></div>
  <div class="abs stat" style="left:263px"><b>455</b><span>Satisfied clients</span></div>
  <div class="abs stat" style="left:499px"><b>100 +</b><span>Professional writers</span></div>
  <div class="abs stat" style="left:735px"><b>1000</b><span>jobs done</span></div>
</section>

<section class="reviews">
  <h2 class="abs">Trusted by 100+<br>students Around<br>the World</h2>
  <p class="abs rated">Rated 4.9 Out Of 5 Based On 1000 Reviews</p>
  <div class="abs fair"><i></i>fair meter</div>
  <div class="abs arrow" style="left:395px"><svg width="8" height="8" viewBox="0 0 8 8"><path d="M5 1L2 4l3 3" stroke="#1F73B7" fill="none"/></svg></div>
  <div class="abs arrow" style="left:429px"><svg width="8" height="8" viewBox="0 0 8 8"><path d="M3 1l3 3-3 3" stroke="#1F73B7" fill="none"/></svg></div>
  <div class="abs rcard" style="left:472px">
    <div class="rs stars">★★★★★</div>
    <h4>Professionalism, Quality</h4>
    <p>Vero eros et accumsan et iusto odio dignissim qui blandit praesent luptatum zzril delenit augue duis dolore te feugait nulla facilisi.</p>
    <div class="who"><i>IO</i>Iusto Odio</div>
  </div>
  <div class="abs rcard" style="left:733px">
    <div class="rs stars">★★★★★</div>
    <h4>Professionalism</h4>
    <p>Facilis odio dignissim qui blandit praesent luptatum zzril delenit augue duis dolore te feugait nulla vero eros accumsan et iusto</p>
    <div class="who"><i>ZD</i>Zzril Delenit</div>
  </div>
  <div class="abs rcard" style="left:995px">
    <div class="rs stars">★★★★★</div>
    <h4>Professionalism</h4>
    <p>zzril delenit augue duis odio dignissim qui blandit praesent luptatum duis accumsan et iusto dolore te feugait nulla vero eros</p>
    <div class="who"><i>VE</i>Vero Eros</div>
  </div>
</section>

<section class="writers">
  <h2 class="title" style="top:58px">An Exclusive Network of Top Writers.</h2>
  <div class="abs wcard" style="left:163px">
    <div class="head"><div class="av" role="img" aria-label="Writer portrait"></div><div class="nm">Vulputate Velit<small>Iusto Odio</small></div></div>
    <div class="body">
      <div class="id">Writer ID = #12345</div>
      <div><span class="k">Rating:</span> <span class="stars">★★★★★</span> 4.5</div>
      <div><span class="k">Punctuality:</span> <b>98%</b></div>
      <div><span class="k">In Progress:</span> <b>2 Orders</b></div>
      <div><span class="k">Completed:</span> <b>50 Orders</b></div>
      <div class="badges"><i></i><i></i><i></i><i></i><i></i></div>
      <div class="vp">VIEW PROFILE</div>
    </div>
  </div>
  <div class="abs wcard" style="left:382px">
    <div class="head"><div class="av" role="img" aria-label="Writer portrait"></div><div class="nm">Exerci Tation<small>Iusto Odio</small></div></div>
    <div class="body">
      <div class="id">Writer ID = #12345</div>
      <div><span class="k">Rating:</span> <span class="stars">★★★★★</span> 4.5</div>
      <div><span class="k">Punctuality:</span> <b>98%</b></div>
      <div><span class="k">In Progress:</span> <b>2 Orders</b></div>
      <div><span class="k">Completed:</span> <b>50 Orders</b></div>
      <div class="badges"><i></i><i></i><i></i><i></i><i></i></div>
      <div class="vp">VIEW PROFILE</div>
    </div>
  </div>
  <div class="abs wcard" style="left:601px">
    <div class="head"><div class="av" role="img" aria-label="Writer portrait"></div><div class="nm">Iriure Dolor<small>Iusto Odio</small></div></div>
    <div class="body">
      <div class="id">Writer ID = #12345</div>
      <div><span class="k">Rating:</span> <span class="stars">★★★★★</span> 4.5</div>
      <div><span class="k">Punctuality:</span> <b>98%</b></div>
      <div><span class="k">In Progress:</span> <b>2 Orders</b></div>
      <div><span class="k">Completed:</span> <b>50 Orders</b></div>
      <div class="badges"><i></i><i></i><i></i><i></i><i></i></div>
      <div class="vp">VIEW PROFILE</div>
    </div>
  </div>
  <div class="abs wcard" style="left:827px">
    <div class="head"><div class="av" role="img" aria-label="Writer portrait"></div><div class="nm">Blandit Praesent<small>Iusto Odio</small></div></div>
    <div class="body">
      <div class="id">Writer ID = #12345</div>
      <div><span class="k">Rating:</span> <span class="stars">★★★★★</span> 4.5</div>
      <div><span class="k">Punctuality:</span> <b>98%</b></div>
      <div><span class="k">In Progress:</span> <b>2 Orders</b></div>
      <div><span class="k">Completed:</span> <b>50 Orders</b></div>
      <div class="badges"><i></i><i></i><i></i><i></i><i></i></div>
      <div class="vp">VIEW PROFILE</div>
    </div>
  </div>
  <a class="btn seeall">See All Professionals</a>
</section>

<section class="features">
  <h2 class="title" style="top:62px;color:#fff">Features &amp; Benefits</h2>
  <div class="abs feat" style="left:222px;top:148px"><span class="ic"><svg width="10" height="10"><path d="M2 8l6-6M5 2h3v3" stroke="#1F73B7" fill="none"/></svg></span><div><h4>Complete access</h4><p>You will always retain full ownership and access to your accounts</p></div></div>
  <div class="abs feat" style="left:500px;top:148px"><span class="ic"><svg width="10" height="10"><circle cx="5" cy="5" r="3" stroke="#1F73B7" fill="none"/></svg></span><div><h4>Honest reporting</h4><p>Reconcilable and transparent reporting with no vanity metrics</p></div></div>
  <div class="abs feat" style="left:783px;top:148px"><span class="ic"><svg width="10" height="10"><path d="M5 1v8M3 3h4M3 7h4" stroke="#1F73B7" fill="none"/></svg></span><div><h4>Fixed Pricing</h4><p>We don't charge 10% of your budget like other companies.</p></div></div>
  <div class="abs feat" style="left:222px;top:296px"><span class="ic"><svg width="10" height="10"><rect x="2" y="1" width="6" height="8" stroke="#1F73B7" fill="none"/></svg></span><div><h4>No long-term contracts</h4><p>You deserve the freedom to do what's right for you</p></div></div>
  <div class="abs feat" style="left:500px;top:296px"><span class="ic"><svg width="10" height="10"><path d="M5 1l3 2v3l-3 3-3-3V3z" stroke="#1F73B7" fill="none"/></svg></span><div><h4>Plagiarism-Free Policy</h4><p>Your campaigns will be monitored and managed by certified experts (not bots!)</p></div></div>
  <div class="abs feat" style="left:783px;top:296px"><span class="ic"><svg width="10" height="10"><circle cx="5" cy="4" r="2" stroke="#1F73B7" fill="none"/><path d="M1.5 9c1-2 6-2 7 0" stroke="#1F73B7" fill="none"/></svg></span><div><h4>You own everything</h4><p>You own all applicable intellectual property</p></div></div>
  <a class="btn" style="left:543px;top:414px;width:112px;height:34px">Order Now</a>
</section>

<section class="why">
  <h2 class="abs">Why Us?</h2>
  <div class="abs wi" style="top:152px"><h4>Proof of Quality</h4><p>Check our Samples, Client Reviews and Identity Verification.</p></div>
  <div class="abs wi" style="top:222px"><h4>Great prices For Superb Quality</h4><p>You Can't Afford to Get Overcharged. Satisfaction is Guaranteed once you order<br>with Us.</p></div>
  <div class="abs wi" style="top:314px"><h4>Safe and Secure</h4><p>We let you focus on your work as we help protect your data and privacy. We are<br>here 24/7 for any support needed.</p></div>
  <div class="abs wi" style="top:406px"><h4>Highest Repeat Client Rate</h4><p>90% Repeat Order Rate as a result of Professionalism and Originality<br>Guaranteed.Below is a call-to-action button</p></div>
  <a class="btn order">Order Now</a>
  <div class="abs photo" role="img" aria-label="Photo of a smiling student in glasses writing at a desk"></div>
</section>

<section class="how">
  <h2 class="title">How it Works</h2>
  <svg class="abs" style="left:0;top:0" width="1200" height="389" aria-hidden="true">
    <g stroke="#6fb8a6" stroke-width="1" fill="none" stroke-dasharray="3 3">
      <path d="M400 148H416M684 148H690M802 148H853M913 168V195M747 218H743M557 240H404M330 262V285H380M592 308H751"/>
      <path d="M480 168V198M480 198H330V215"/>
    </g>
  </svg>
  <div class="pill" style="left:226px;top:128px;width:174px;height:40px">Choose One Of The 2<br>Available Option</div>
  <div class="pill" style="left:416px;top:128px;width:268px;height:40px">Provide Us With The Details Of Your Paper By<br>Filling The Order From</div>
  <div class="pill" style="left:690px;top:128px;width:112px;height:40px">Make Payment</div>
  <div class="pill" style="left:853px;top:128px;width:121px;height:40px">Company Choose<br>Writing Behalf</div>
  <div class="pill" style="left:747px;top:195px;width:216px;height:47px">Our Editing Department Check Completed<br>Paper For Grammer, Paragraph, Instructions<br>And Formatting Compliance</div>
  <div class="pill" style="left:257px;top:215px;width:147px;height:47px">Choose Your Prefered<br>Writer</div>
  <div class="pill" style="left:557px;top:218px;width:186px;height:44px">Release Money Only When<br>Satisfied</div>
  <div class="pill" style="left:380px;top:285px;width:212px;height:47px">Make A Deposit And Your Writer Will Start<br>Working On Your Paper</div>
  <div class="pill final" style="left:751px;top:271px;width:145px;height:57px">Final Delivery And<br>Rate The Work</div>
</section>

<section class="welcome">
  <h2 class="title">Welcome to<br>FindSterlingEssays</h2>
  <div class="abs sub">Top Research &amp; Summary Writing Service.</div>
  <p class="abs">sed diam nonummy nibh euismod tincidunt ut laoreet dolore magna aliquam erat volutpat. Ut wisi enim ad minim veniam, quis nostrud exerci tation ullamcorper suscipit lobortis nisl ut aliquip ex ea commodo consequat. Duis autem vel eum iriure dolor in hendrerit in vulputate velit esse molestie consequat, vel illum dolore eu feugiat nulla facilisis at vero eros et accumsan et iusto odio dignissim qui blandit praesent luptatum zzril delenit augue duis dolore te feugait nulla facilisi.</p>
</section>

<section class="brief">
  <div class="abs panel"><span class="dash"></span></div>
  <div class="abs bcard" style="left:280px"><span class="bar"></span>
    <h4>Top Research &amp; Summary Writing Service.</h4>
    <p>sed diam nonummy nibh euismod tincidunt ut laoreet dolore magna aliquam erat volutpat. Ut wisi enim ad minim veniam, quis nostrud exerci tation ullamcorper suscipit lobortis nisl ut aliquip ex ea commodo consequat. Duis autem vel eum iriure dolor in hendrerit in vulputate velit esse molestie consequat, vel illum dolore eu feugiat nulla facilisis at vero eros et accumsan et iusto odio dignissim qui blandit praesent luptatum zzril delenit augue duis dolore te feugait nulla facilisi.</p>
  </div>
  <div class="abs bcard" style="left:600px"><span class="bar"></span>
    <h4>Top Research &amp; Summary Writing Service.</h4>
    <p>sed diam nonummy nibh euismod tincidunt ut laoreet dolore magna aliquam erat volutpat. Ut wisi enim ad minim veniam, quis nostrud exerci tation ullamcorper suscipit lobortis nisl ut aliquip ex ea commodo consequat. Duis autem vel eum iriure dolor in hendrerit in vulputate velit esse molestie consequat, vel illum dolore eu feugiat nulla facilisis at vero eros et accumsan et iusto odio dignissim qui blandit praesent luptatum zzril delenit augue duis dolore te feugait nulla facilisi.</p>
  </div>
</section>

<section class="faq">
  <h2 class="title">FAQs</h2>
  <div class="abs q" style="left:244px;top:120px"><i>?</i><div><h4>Do et accumsan et iusto odio dignissim qui?</h4><p>Yes, ipsum iriure dolor in hendrerit</p></div></div>
  <div class="abs q" style="left:244px;top:190px"><i>?</i><div><h4>For how long eum iriure dolor in hendrerit?</h4><p>You are not team iriure dolor in hendrerit eum iriure dolor in hendrerit</p></div></div>
  <div class="abs q" style="left:244px;top:280px"><i>?</i><div><h4>How do I know your accumsan et?</h4><p>accumsan et iusto odio dignissim qui blandit praesent</p></div></div>
  <div class="abs q" style="left:244px;top:348px"><i>?</i><div><h4>How do I accumsan et iusto?</h4><p>zzril delenit augue duis dolore te feugait nulla facilisi</p></div></div>
  <div class="abs q" style="left:244px;top:418px"><i>?</i><div><h4>How blandit praesent luptatum ?</h4><p>dignissim qui blandit praesent luptatum zzril delenit augue duis dolore te feugait nulla facilisi</p></div></div>
  <div class="abs q" style="left:624px;top:120px"><i>?</i><div><h4>Do you blandit praesent luptatum zzril delenit augue duis dolore?</h4><p>No. We specialize and only eum iriure dolor in hendrerit</p></div></div>
  <div class="abs q" style="left:624px;top:210px"><i>?</i><div><h4>Is my accumsan et iusto odio dignissim ?</h4><p>accumsan et iusto odio dignissim qui blandit praesent luptatum zzril delenit augue duis dolore te feugait nulla facilisi</p></div></div>
  <div class="abs q" style="left:624px;top:298px"><i>?</i><div><h4>Is my te feugait nulla facilisi?</h4><p>luptatum zzril delenit augue duis dolore te feugait nulla facilisi</p></div></div>
  <div class="abs q" style="left:624px;top:376px"><i>?</i><div><h4>Is my ignissim qui blandit ?</h4><p>blandit praesent luptatum zzril delenit augue duis dolore te</p></div></div>
  <div class="abs q" style="left:624px;top:452px"><i>?</i><div><h4>Is my it praesent luptatum zzril ?</h4><p>accumsan et iusto odio dignissim qui blandit praesent luptatum zzril delenit augue duis dolore te feugait nulla facilisi</p></div></div>
</section>

<section class="keys">
  <h2 class="title">Keywords</h2>
  <div class="abs kw" style="left:163px;top:148px">Essay</div>
  <div class="abs kw" style="left:390px;top:148px">Literature Review</div>
  <div class="abs kw" style="left:615px;top:148px">Admission Essay</div>
  <div class="abs kw" style="left:840px;top:148px">Case Study</div>
  <div class="abs kw" style="left:163px;top:216px">Business Plan</div>
  <div class="abs kw" style="left:390px;top:216px">Creative Writing</div>
  <div class="abs kw" style="left:615px;top:216px">Report</div>
  <div class="abs kw" style="left:840px;top:216px">Research Proposal</div>
  <div class="abs kw" style="left:163px;top:279px">Critical Thinking / Review</div>
  <div class="abs kw" style="left:390px;top:279px">Research Paper</div>
  <div class="abs kw" style="left:615px;top:279px">Book / Movie Review</div>
  <div class="abs kw" style="left:840px;top:279px">Book Reviews</div>
  <div class="abs kw" style="left:163px;top:342px">Presentation or Speech</div>
  <div class="abs kw" style="left:390px;top:342px">Editing and proofreading</div>
  <div class="abs kw" style="left:615px;top:342px">Term Paper</div>
  <div class="abs kw" style="left:840px;top:342px">Annotated Bibliography</div>
</section>

<footer>
  <div class="abs guar">Guarantee</div>
  <div class="abs gbox" style="left:372px"><svg width="22" height="24" viewBox="0 0 22 24"><rect x="3" y="2" width="16" height="20" rx="1" stroke="#fff" fill="none"/><path d="M7 8h8M7 12h8M7 16h5" stroke="#fff"/></svg>Revision</div>
  <div class="abs gbox" style="left:580px"><svg width="26" height="22" viewBox="0 0 26 22"><rect x="2" y="4" width="14" height="16" stroke="#fff" fill="none"/><path d="M6 9h6M6 13h6M6 17h6" stroke="#fff"/><circle cx="20" cy="15" r="4" stroke="#fff" fill="none"/></svg>Money Back</div>
  <div class="abs gbox" style="left:786px"><svg width="24" height="24" viewBox="0 0 24 24"><path d="M3 13L13 3h8v8L11 21z" stroke="#fff" fill="none"/><circle cx="17" cy="7" r="1.5" fill="#fff"/></svg>Plagiarism Free</div>
  <div class="abs flogo">FindSterlingEssays<small>Writing platform</small></div>
  <p class="abs fabout">Sed diam nonummy nibh euismod tincidunt ut laoreet dolore magna aliquam erat volutpat. Ut wisi enim ad minim veniam, quis nostrud exerci tation ullamcorper suscipit lobortis nisl ut aliquip ex ea commodo consequat.</p>
  <div class="abs flinks">Cookie Policy<br>Privacy Policy<br>Confidentiality Policy<br>Revision Policy<br>Deposit &amp; Refund Policy<br>Plagiarism-free Policy<br>Progressive Delivery<br>Terms &amp; Conditions</div>
  <div class="abs fcontact">
    <div><svg width="10" height="13" viewBox="0 0 10 13"><path d="M5 12S1 7 1 5a4 4 0 018 0c0 2-4 7-4 7z" stroke="#fff" fill="none"/><circle cx="5" cy="5" r="1.4" fill="#fff"/></svg><span>Duis autem vel02<br>eum iriure</span></div>
    <div><svg width="11" height="11" viewBox="0 0 11 11"><path d="M2 1l2 .5.8 2.5-1.3 1a6 6 0 002.5 2.5l1-1.3 2.5.8.5 2c-5 1-9-3-8-8z" fill="#fff"/></svg><span>555 010 2468</span></div>
    <div><svg width="12" height="9" viewBox="0 0 12 9"><rect x=".5" y=".5" width="11" height="8" stroke="#fff" fill="none"/><path d="M1 1l5 4 5-4" stroke="#fff" fill="none"/></svg><span>info@findsterlingessays.example</span></div>
  </div>
  <div class="abs copy">© 2022 FindSterlingEssays. All rights reserved.</div>
</footer>

</body>
</html>
```